Vela Stewardship Business Card design

We need a creative business card design for our hospitality management company
We need the following information:
Our business Logo: Vela Stewardship
Name: Mara Dobrinsky
Phone number: 0458 317 642
Email: mara@velastewardship.com.au
Address: 214/53 Penrose Street, South Melbourne 3206
Web: www.velastewardship.com.au
I need the design to be a working file so that I can insert the names and numbers of the other staff members of our business.
The cards need to be 90 x 40mm
Thanks
Industry/Entity Type
Hospitality
Look and feel

```html
<!DOCTYPE html>
<html lang="en">
<head>
<meta charset="utf-8">
<title>Vela Stewardship Business Card</title>
<link rel="stylesheet" href="https://fonts.googleapis.com/css2?family=Arimo:wght@400;700&display=swap">
<style>
  :root {
    --backdrop: #ece8e2;
    --card: #231d33;
    --ink-light: #ffffff;
    --ink-accent: #9caadf;
    --mark: #e9e9ee;
  }
  * { margin: 0; padding: 0; box-sizing: border-box; }
  html, body {
    width: 1200px;
    height: 1000px;
    overflow: hidden;
    background: var(--backdrop);
    font-family: "Arimo", Arial, sans-serif;
  }
  .sheet {
    position: relative;
    width: 1200px;
    height: 1000px;
  }
  .card {
    position: absolute;
    top: 210px;
    width: 320px;
    height: 580px;
    background: var(--card);
    box-shadow: 0 3px 10px rgba(0,0,0,0.18);
  }
  .card--front { left: 230px; }
  .card--back { left: 650px; }

  .brand {
    position: absolute;
    display: flex;
    align-items: center;
    gap: 10px;
    color: var(--mark);
    font-weight: 700;
    text-transform: uppercase;
    white-space: nowrap;
  }
  .brand__square {
    display: block;
    background: var(--mark);
  }
  .card--front .brand {
    left: 0;
    right: 0;
    bottom: 70px;
    flex-direction: column;
    gap: 14px;
    font-size: 22px;
    letter-spacing: 0.5px;
  }
  .card--front .brand__square { width: 60px; height: 60px; }
  .card--back .brand {
    top: 40px;
    right: 32px;
    font-size: 11px;
    letter-spacing: 0.4px;
  }
  .card--back .brand__square { width: 30px; height: 30px; }

  .contact {
    position: absolute;
    left: 40px;
    bottom: 62px;
    color: var(--ink-light);
  }
  .contact__name {
    color: var(--ink-accent);
    font-size: 24px;
    font-weight: 400;
    letter-spacing: 0.5px;
    margin-bottom: 26px;
  }
  .contact__line {
    font-size: 14px;
    line-height: 19px;
  }
  .contact__group { margin-bottom: 14px; }
  .contact__web {
    color: var(--ink-accent);
    font-size: 14px;
  }
</style>
</head>
<body>
<main class="sheet">
  <section class="card card--front" aria-label="Card front">
    <div class="brand">
      <span class="brand__square"></span>
      <span class="brand__name">Vela Stewardship</span>
    </div>
  </section>

  <section class="card card--back" aria-label="Card back">
    <div class="brand">
      <span class="brand__name">Vela Stewardship</span>
      <span class="brand__square"></span>
    </div>
    <div class="contact">
      <h1 class="contact__name">Mara Dobrinsky</h1>
      <div class="contact__group">
        <p class="contact__line">0458 317 642</p>
        <p class="contact__line">mara@velastewardship.com.au</p>
      </div>
      <div class="contact__group">
        <p class="contact__line">214/53 Penrose Street,</p>
        <p class="contact__line">South Melbourne 3206</p>
      </div>
      <p class="contact__web">www.velastewardship.com.au</p>
    </div>
  </section>
</main>
</body>
</html>
```